Church needs an introductory/informative postcard

We are looking for a postcard that would introduce our church along with having our programing information. We need it to be in Spanish, I can provide the necessary translation. Please provide us with ideas for a tag line that invites people to come check us out. We can provide a bible scripture if necessary, but would like something short that projects interest and confidence. We have a logo that we would like incorporated.

Target Market(s)

Hispanic

Industry/Entity Type

Religious

Requirements
Must have
• Colorful to coordinate with our logo so it flows well
• Have an tag line that invites people to our church
Nice to have
• have a modern feel
• if needed we can provide some pictures of our building
Should not have
• Pictures of people

```html
<!DOCTYPE html>
<html lang="en">
<head>
<meta charset="UTF-8">
<title>Church Postcard – Everyone Is Loved</title>
<link href="https://fonts.googleapis.com/css2?family=Anton&family=Archivo+Black&display=swap" rel="stylesheet">
<style>
  :root {
    --ink: #0b0b0b;
    --glow: #ffffff;
    --loved: #ff4a12;
    --accent-line: #7cc242;
    --paper: #ffffff;
    --brand: #5e2a86;
    --scene-light: #b9f0c8;
    --scene-mid: #3fae7a;
    --scene-deep: #0f3d2a;
    --scene-dark: #061a12;
  }
  * { margin: 0; padding: 0; box-sizing: border-box; }
  html, body {
    width: 1200px;
    height: 900px;
    overflow: hidden;
    background: var(--paper);
  }
  .postcard {
    position: relative;
    width: 1200px;
    height: 900px;
    background: var(--paper);
  }
  .hero {
    position: absolute;
    left: 0;
    top: 0;
    width: 1200px;
    height: 694px;
    background:
      radial-gradient(ellipse 520px 360px at 640px 300px, var(--scene-light) 0%, rgba(120,210,160,0.6) 35%, rgba(63,174,122,0) 75%),
      linear-gradient(180deg, #5fc69a 0%, var(--scene-mid) 40%, var(--scene-deep) 75%, var(--scene-dark) 100%);
  }
  .hero-text {
    position: absolute;
    left: 0;
    top: 0;
    width: 1200px;
    text-align: center;
  }
  .tagline-lead {
    position: absolute;
    left: 0;
    top: 205px;
    width: 1200px;
    font-family: "Anton", sans-serif;
    font-size: 78px;
    line-height: 1;
    letter-spacing: 3px;
    color: var(--ink);
    text-shadow: 0 0 6px var(--glow), 0 0 10px var(--glow), 0 0 16px rgba(255,255,255,0.8);
  }
  .tagline-key {
    position: absolute;
    left: 0;
    top: 292px;
    width: 1200px;
    font-family: "Archivo Black", sans-serif;
    font-size: 262px;
    line-height: 1;
    letter-spacing: -2px;
    color: var(--loved);
    -webkit-text-stroke: 9px var(--glow);
    paint-order: stroke fill;
  }
  .divider {
    position: absolute;
    left: 0;
    top: 694px;
    width: 1200px;
    height: 8px;
    background: var(--accent-line);
  }
  .brand {
    position: absolute;
    left: 0;
    top: 760px;
    width: 1200px;
    display: flex;
    justify-content: center;
    align-items: center;
    gap: 16px;
  }
  .brand-mark {
    width: 58px;
    height: 58px;
    border-radius: 50%;
    background: var(--brand);
  }
  .brand-name {
    font-family: "Anton", sans-serif;
    font-size: 56px;
    line-height: 1;
    letter-spacing: 4px;
    color: var(--brand);
  }
</style>
</head>
<body>
  <main class="postcard">
    <div class="hero" role="img" aria-label="Worship crowd with raised hands in silhouette under glowing green stage light"></div>
    <div class="hero-text">
      <p class="tagline-lead">A CHURCH WHERE EVERYONE IS</p>
      <h1 class="tagline-key">LOVED</h1>
    </div>
    <div class="divider"></div>
    <div class="brand">
      <span class="brand-mark"></span>
      <span class="brand-name">ELIORA</span>
    </div>
  </main>
</body>
</html>
```